Bref créative
VMB Associates, LLC.Business Card, Stationery,
Envelops,letterhead and fax cover
Professional
Dorian Walsby
President
4720 Hollowmere Parkway
Suite 382
Duluth, Ga. 30418
dwalsby@vmbgroupmail.net
www.vmb-partners-example.com
Please no dark background color. Light gray is acceptable.
This will include the services we offer. Telecom Regulatory, Tax Compliance, Corporate Services, Property Tax and Registered Agent Service
We would like the tag line: Accurate, Efficient On Time some where on the card front or back.
we want to get new business and need a card that will make clients want to contact us. Thank you in advance.

```html
<!DOCTYPE html>
<html lang="en">
<head>
<meta charset="utf-8">
<title>VMB Partners, LLC. — Business Card</title>
<link href="https://fonts.googleapis.com/css2?family=Arimo:ital,wght@0,400;0,700;1,400&display=swap" rel="stylesheet">
<style>
  :root {
    --page-bg: #e4e5e7;
    --card-bg: #f6f6f7;
    --card-shade: #e9eaec;
    --brand-blue: #1f7fc8;
    --brand-navy: #123f73;
    --ink: #2b2b2b;
    --ink-soft: #555a60;
    --rule: #b9bcc1;
  }
  * { box-sizing: border-box; margin: 0; padding: 0; }
  html, body { width: 1200px; height: 755px; overflow: hidden; }
  body {
    background: var(--page-bg);
    font-family: "Arimo", Arial, sans-serif;
    color: var(--ink);
    position: relative;
  }
  .card {
    position: absolute;
    width: 550px;
    height: 290px;
    border-radius: 16px;
    background: linear-gradient(180deg, #ffffff 0%, var(--card-bg) 55%, var(--card-shade) 100%);
    box-shadow: 0 6px 18px rgba(0,0,0,0.18);
    overflow: hidden;
  }
  .card-front { left: 240px; top: 80px; }
  .card-back  { left: 420px; top: 410px; }

  .brand-name {
    position: absolute;
    font-weight: 700;
    font-size: 22px;
    line-height: 1;
    color: var(--brand-navy);
    white-space: nowrap;
  }
  .card-front .brand-name { left: 34px; top: 128px; }
  .card-back .brand-name { left: 34px; top: 118px; }

  .divider {
    position: absolute;
    left: 278px; top: 30px;
    width: 1px; height: 190px;
    background: var(--rule);
  }
  .contact { position: absolute; left: 292px; top: 30px; }
  .contact-name { color: var(--brand-blue); font-weight: 700; font-size: 19px; }
  .contact-title { font-style: italic; font-size: 13px; color: var(--ink-soft); margin-top: 2px; }
  .contact-address { font-size: 11.5px; line-height: 1.4; margin-top: 16px; color: var(--ink); }
  .contact-lines { list-style: none; margin-top: 8px; font-size: 11.5px; }
  .contact-lines li { display: flex; align-items: center; gap: 7px; height: 19px; }
  .contact-lines svg { width: 12px; height: 12px; flex: none; }

  .band { position: absolute; left: 0; right: 0; bottom: 0; height: 34px; }
  .band-top { position: absolute; left: 0; right: 0; top: 0; height: 3px; background: var(--brand-navy); }
  .band-main { position: absolute; left: 0; right: 0; top: 6px; height: 16px; background: var(--brand-blue); }
  .band-low { position: absolute; left: 0; right: 0; top: 24px; height: 10px; background: var(--brand-navy); }
  .web {
    position: absolute; right: 22px; bottom: 40px;
    font-size: 11px; color: var(--ink-soft);
  }

  .services { position: absolute; left: 292px; top: 34px; list-style: none; }
  .services li {
    display: flex; align-items: center; gap: 9px;
    font-size: 14.5px; height: 26px; color: var(--ink);
  }
  .services svg { width: 13px; height: 13px; flex: none; }
  .tagline {
    position: absolute; left: 292px; bottom: 60px;
    font-weight: 700; font-size: 18px; color: var(--ink);
  }
</style>
</head>
<body>

<section class="card card-front" aria-label="Business card front">
  <p class="brand-name">VMB Partners, LLC.</p>
  <div class="divider"></div>
  <div class="contact">
    <p class="contact-name">Dorian Walsby</p>
    <p class="contact-title">President</p>
    <p class="contact-address">4720 Hollowmere Parkway<br>Suite 382<br>Duluth, Ga. 30418</p>
    <ul class="contact-lines">
      <li><svg viewBox="0 0 12 12"><path d="M3 1h2l1 3-1.5 1a6 6 0 0 0 2.5 2.5L8 6l3 1v2a2 2 0 0 1-2 2A8 8 0 0 1 1 3a2 2 0 0 1 2-2z" fill="var(--brand-navy)"/></svg>678-555-0142</li>
      <li><svg viewBox="0 0 12 12"><rect x="3" y="0.5" width="6" height="11" rx="1" fill="var(--brand-navy)"/><rect x="4" y="2" width="4" height="6" fill="#fff"/></svg>404-555-0187</li>
      <li><svg viewBox="0 0 12 12"><rect x="1" y="4" width="10" height="6" rx="1" fill="var(--brand-navy)"/><rect x="3" y="1" width="6" height="4" fill="var(--brand-navy)"/><rect x="3" y="7" width="6" height="1" fill="#fff"/></svg>888-555-0163</li>
      <li><svg viewBox="0 0 12 12"><rect x="0.5" y="2" width="11" height="8" rx="1" fill="var(--brand-navy)"/><path d="M1 3l5 4 5-4" stroke="#fff" fill="none"/></svg>dwalsby@vmbgroupmail.net</li>
    </ul>
  </div>
  <p class="web">www.vmb-partners-example.com</p>
  <div class="band"><div class="band-top"></div><div class="band-main"></div><div class="band-low"></div></div>
</section>

<section class="card card-back" aria-label="Business card back">
  <p class="brand-name">VMB Partners, LLC.</p>
  <ul class="services">
    <li><svg viewBox="0 0 13 13"><rect width="13" height="13" rx="2" fill="var(--brand-blue)"/><path d="M4 3l4 3.5L4 10" stroke="#fff" stroke-width="1.8" fill="none"/></svg>Telecom Regulatory</li>
    <li><svg viewBox="0 0 13 13"><rect width="13" height="13" rx="2" fill="var(--brand-blue)"/><path d="M4 3l4 3.5L4 10" stroke="#fff" stroke-width="1.8" fill="none"/></svg>Tax Compliance</li>
    <li><svg viewBox="0 0 13 13"><rect width="13" height="13" rx="2" fill="var(--brand-blue)"/><path d="M4 3l4 3.5L4 10" stroke="#fff" stroke-width="1.8" fill="none"/></svg>Corporate Services</li>
    <li><svg viewBox="0 0 13 13"><rect width="13" height="13" rx="2" fill="var(--brand-blue)"/><path d="M4 3l4 3.5L4 10" stroke="#fff" stroke-width="1.8" fill="none"/></svg>Property Tax</li>
    <li><svg viewBox="0 0 13 13"><rect width="13" height="13" rx="2" fill="var(--brand-blue)"/><path d="M4 3l4 3.5L4 10" stroke="#fff" stroke-width="1.8" fill="none"/></svg>Registered Agent Service</li>
  </ul>
  <p class="tagline">Accurate, Efficient On Time</p>
</section>

</body>
</html>
```